Modern solo law firm website

I am preparing to launch a solo law practice (I own the domain varrowcounsel.com and/or may use Varrow Law Office as a dba), and will need to move quickly to put up a website once I pull the trigger. There are many existing law firm sites to "copy," but I'm looking for something a little more modern and unique with some scrolling and modern icons (see e.g., telbriclaw.com). Right now, need the logo and skeleton for the site, as I have not written all of the content. For now, I like the idea of a simple home page that incorporates the phrase "Impactful. Valuable. Trusted." (Again, I may change that text.) And would like links on the home page across the top for "about", "services", "people" and "contact" -- these should lead to separate landing pages. The bottom of the home page also should have a link for a "disclaimer" and to Facebook, Twitter and LinkedIn (which I have not yet created). Make sense? Let me know if you have questions.

Target Market(s)

Business clients

Industry/Entity Type

Law Firm

Number of Pages Required

5+ page

Font styles to use
Other font styles liked:
• Perhaps Segoe UI

Requirements
Must have
• DRAFT STRUCTURE AND TEXT NOW ATTACHED. HOWEVER, SUBJECT TO EDITS BEING MADE CONCURRENTLY.

```html
<!DOCTYPE html>
<html lang="en">
<head>
<meta charset="utf-8">
<title>Varrow Law Office</title>
<link href="https://fonts.googleapis.com/css2?family=Questrial&display=swap" rel="stylesheet">
<style>
:root{
  --accent:#e8664a;
  --hero-top:#d2644b;
  --hero-bottom:#b8492f;
  --light:#efefef;
  --ink:#333333;
  --body:#444444;
  --footer:#2e2e2e;
  --white:#ffffff;
  --muted:#d8d8d8;
}
*{box-sizing:border-box;margin:0;padding:0}
html,body{width:799px;height:1200px;overflow:hidden}
body{position:relative;font-family:"Questrial",sans-serif;color:var(--ink);background:var(--white)}

/* Hero */
.hero{position:absolute;left:0;top:0;width:799px;height:290px;overflow:hidden}
.hero-image{position:absolute;inset:0;background:radial-gradient(ellipse at 60% 40%,#e07a5f 0%,var(--hero-top) 45%,var(--hero-bottom) 100%)}
.brand{position:absolute;left:0;top:40px;width:799px;display:flex;justify-content:center;align-items:center;gap:10px;color:var(--white);font-size:22px;line-height:26px}
.brand-mark{width:14px;height:14px;background:var(--white)}
.main-nav{position:absolute;top:131px;left:0;width:799px;height:26px}
.main-nav a{position:absolute;top:0;height:26px;line-height:26px;font-size:14px;color:var(--white);text-decoration:none}
.main-nav a.current{background:rgba(232,102,74,.85);color:#222;padding:0 8px;box-shadow:0 1px 3px rgba(0,0,0,.25)}
.hero-kicker{position:absolute;top:194px;width:799px;text-align:center;color:var(--white);font-size:26px}
.hero-quote{position:absolute;top:230px;width:799px;text-align:center;color:var(--white);font-size:21px}
.hero-quote .big{font-size:29px}

/* Intro */
.intro{position:absolute;left:0;top:290px;width:799px;height:224px;background:var(--light);text-align:center}
.intro h1{position:absolute;top:26px;width:799px;font-weight:400;font-size:19px;color:var(--ink)}
.intro h1 .hl{color:var(--accent)}
.intro p{position:absolute;top:58px;width:799px;font-size:14px;line-height:23.3px;color:var(--body)}
.btn{position:absolute;top:167px;width:120px;height:30px;line-height:30px;background:var(--accent);color:var(--white);font-size:14px;border-radius:4px;text-decoration:none;box-shadow:0 1px 2px rgba(0,0,0,.2)}

/* Values */
.values{position:absolute;left:0;top:514px;width:799px;height:194px;background:linear-gradient(180deg,#505050,#444444);color:var(--white)}
.values h2{position:absolute;top:24px;width:799px;text-align:center;font-weight:400;font-size:26px}
.value{position:absolute;top:76px;width:180px;text-align:center}
.value svg{display:block;margin:0 auto;width:50px;height:50px}
.value span{display:block;margin-top:8px;font-size:27px}

/* Services */
.services h2{position:absolute;top:728px;width:799px;text-align:center;font-weight:400;font-size:26px;color:var(--ink)}
.service{position:absolute;width:280px;height:75px}
.service-photo{position:absolute;left:0;top:0;width:112px;height:75px}
.service-title{position:absolute;left:115px;top:2px;font-size:13px;color:var(--ink);white-space:nowrap;display:flex;align-items:center;gap:4px}
.service-title svg{width:16px;height:16px}
.service-text{position:absolute;left:115px;top:24px;width:164px;font-size:9.4px;line-height:12.6px;color:var(--body);text-align:justify;overflow:hidden;height:52px}

/* Footer */
.site-footer{position:absolute;left:0;top:984px;width:799px;height:180px;background:var(--footer);color:var(--white)}
.divider{position:absolute;top:20px;width:1px;height:140px;background:#888}
.f-head{position:absolute;font-size:12px}
.f-text{position:absolute;font-size:9.5px;line-height:12.5px;color:var(--muted)}
.social{position:absolute;top:46px;left:299px;display:flex;gap:6px}
.social a{display:block;width:20px;height:20px;border-radius:3px;background:var(--accent)}
.field{position:absolute;background:var(--white);color:#333;font-size:8.5px;padding:3px 2px}
.field-label{position:absolute;font-size:9.5px;text-align:right;width:44px}
.send{position:absolute;left:644px;top:140px;width:48px;height:20px;line-height:20px;text-align:center;background:var(--accent);font-size:12px}
.copyright{position:absolute;left:0;top:1164px;width:799px;height:36px;background:var(--accent);color:var(--white);font-size:9.5px;line-height:36px;padding-left:108px}
</style>
</head>
<body>

<header class="hero">
  <div class="hero-image" role="img" aria-label="Warm orange-toned photo of a judge's gavel and scales of justice"></div>
  <div class="brand"><span class="brand-mark"></span><span class="brand-name">Varrow Law Office</span></div>
  <nav class="main-nav">
    <a class="current" href="#" style="left:188px">HOME</a>
    <a href="#" style="left:266px">ABOUT US</a>
    <a href="#" style="left:365px">SERVICE</a>
    <a href="#" style="left:452px">PEOPLE</a>
    <a href="#" style="left:534px">CONTATC US</a>
  </nav>
  <div class="hero-kicker">So True</div>
  <div class="hero-quote">“<span class="big">LAW</span> can not be for one side alone but must be for both...!”</div>
</header>

<section class="intro">
  <h1><span class="hl">Big Law</span> Plays An Important Part In The Legal Services Industry.</h1>
  <p>While you get the resources of a large organization, the services are costly and<br>
  mis-incentivized so your lawyers benefit from taking longer and chasing every angle,<br>
  regardless of whether it makes the most sense for your needs and budget.<br>
  Been there, seen that.</p>
  <a class="btn" href="#" style="left:283px">READ MORE</a>
  <a class="btn" href="#" style="left:419px">CONTACT US</a>
</section>

<section class="values">
  <h2>We Believe in</h2>
  <div class="value" style="left:115px">
    <svg viewBox="0 0 50 50" fill="none" stroke="#fff" stroke-width="2.4" stroke-linecap="round">
      <line x1="25" y1="6" x2="25" y2="42"/><line x1="8" y1="12" x2="42" y2="12"/>
      <line x1="16" y1="44" x2="34" y2="44"/>
      <path d="M10 12 L3 28 H17 Z" fill="#fff"/><path d="M40 12 L33 28 H47 Z" fill="#fff"/>
    </svg>
    <span>Impactful</span>
  </div>
  <div class="value" style="left:325px">
    <svg viewBox="0 0 50 50" fill="#fff">
      <rect x="20" y="2" width="14" height="22" rx="2" transform="rotate(45 27 13)"/>
      <rect x="6" y="24" width="4" height="22" transform="rotate(45 8 35)"/>
      <rect x="24" y="44" width="24" height="4"/>
    </svg>
    <span>Valuable</span>
  </div>
  <div class="value" style="left:529px">
    <svg viewBox="0 0 50 50" fill="none" stroke="#fff" stroke-width="2.6" stroke-linejoin="round">
      <path d="M4 18 L14 10 L24 16 L34 10 L46 18 L38 32 L28 40 L18 36 L10 30 Z" fill="#fff"/>
      <path d="M14 24 L24 32 M20 20 L30 28" stroke="#4a4a4a"/>
    </svg>
    <span>Trust</span>
  </div>
</section>

<section class="services">
  <h2>Services</h2>

  <article class="service" style="left:108px;top:780px">
    <div class="service-photo" role="img" aria-label="Photo of a lawyer meeting with business clients" style="background:linear-gradient(135deg,#6d5a4a,#b49a80)"></div>
    <div class="service-title"><svg viewBox="0 0 16 16"><rect x="1" y="3" width="14" height="11" rx="1" fill="#e8664a"/><rect x="5" y="1" width="6" height="3" fill="none" stroke="#e8664a" stroke-width="1.5"/></svg>Outside General Counsel</div>
    <p class="service-text">Regular interaction with your business and key decision makers as well as Proactive identification and preventive mitigation of legal exposures and risk.</p>
  </article>

  <article class="service" style="left:416px;top:780px">
    <div class="service-photo" role="img" aria-label="Photo of hands reviewing documents with a pen" style="background:linear-gradient(135deg,#4d6a88,#c7d3de)"></div>
    <div class="service-title"><svg viewBox="0 0 16 16"><path d="M8 1a5 5 0 0 1 5 5c0 4-5 9-5 9S3 10 3 6a5 5 0 0 1 5-5z" fill="#e8664a"/><circle cx="8" cy="6" r="2" fill="#fff"/></svg>Litigation&nbsp; resolution</div>
    <p class="service-text">Antitrust and business competition, Intellectual property and technology, o Digital privacy and advertising as well as o Breach of contract</p>
  </article>

  <article class="service" style="left:108px;top:882px">
    <div class="service-photo" role="img" aria-label="Photo of business people standing in a group" style="background:linear-gradient(135deg,#8a8f94,#e2e4e6)"></div>
    <div class="service-title"><svg viewBox="0 0 16 16" fill="#e8664a"><circle cx="8" cy="5" r="2.5"/><circle cx="3" cy="6" r="2"/><circle cx="13" cy="6" r="2"/><path d="M3 14a5 5 0 0 1 10 0z"/></svg>Employment Consulting.</div>
    <p class="service-text">Regular interaction with your business and key decision makers as well as Proactive identification and preventive mitigation of legal exposures and risk.</p>
  </article>

  <article class="service" style="left:416px;top:882px">
    <div class="service-photo" role="img" aria-label="Photo of a person signing business papers at a laptop" style="background:linear-gradient(135deg,#2f3a4a,#d9dde2)"></div>
    <div class="service-title"><svg viewBox="0 0 16 16"><rect x="3" y="1" width="10" height="14" rx="1" fill="none" stroke="#e8664a" stroke-width="1.6"/><line x1="5.5" y1="6" x2="10.5" y2="6" stroke="#e8664a"/><line x1="5.5" y1="9" x2="10.5" y2="9" stroke="#e8664a"/></svg>Business Documents.</div>
    <p class="service-text">Antitrust and business competition, Intellectual property and technology, o Digital privacy and advertising as well as o Breach of contract</p>
  </article>
</section>

<footer class="site-footer">
  <div class="f-head" style="left:108px;top:16px">Contact Us</div>
  <div class="f-head" style="left:108px;top:44px">Varrow Law Office</div>
  <div class="f-text" style="left:108px;top:66px">2240 Larkmoor Street<br>Denver, Colorado 80205</div>
  <div class="f-text" style="left:108px;top:98px">Call: 000 000 000<br>Email:&nbsp; info@varrowcounsel.com</div>

  <div class="divider" style="left:265px"></div>

  <div class="f-head" style="left:299px;top:18px">Get in Touch with Us</div>
  <div class="social">
    <a href="#" aria-label="Social profile one"></a>
    <a href="#" aria-label="Social profile two"></a>
    <a href="#" aria-label="Social profile three"></a>
    <a href="#" aria-label="Social profile four"></a>
  </div>
  <div class="f-head" style="left:299px;top:84px">Newsletter Subscription</div>
  <div class="field" style="left:299px;top:103px;width:148px;height:19px">Enter your Email</div>

  <div class="divider" style="left:475px"></div>

  <div class="f-head" style="left:499px;top:20px">Quick Contact to us</div>
  <div class="field-label" style="left:496px;top:48px">Name:</div>
  <div class="field" style="left:542px;top:44px;width:149px;height:20px">Enter your Name</div>
  <div class="field-label" style="left:496px;top:77px">Email:</div>
  <div class="field" style="left:542px;top:73px;width:149px;height:20px">Enter your Email</div>
  <div class="field-label" style="left:496px;top:105px">Message:</div>
  <div class="field" style="left:542px;top:101px;width:149px;height:34px">Enter your Meage</div>
  <div class="send">Send</div>
</footer>

<div class="copyright">© 2014 Varrow Law Office. All Rights Reserved.</div>

</body>
</html>
```